Bottle Label for Aurum Select CBD Oil

10 ml CBD-Oil bottle. The job is pretty straight forward and everything you need is prepared. However, the design part of the creative part ^^ The design of a lot of follow-up products we could do together. We thought about an exclusive / minimalist approach to Brindle. The bottle itself is delivered in a drawer box which looks much better than the cheap packages of the competition. Everything about the product is supposed to be honest and of high quality. The product is even more cost-effective than CBD-Oils. Key feature of the product is its deeply golden color. The design should be in harmony with this color. The customer pays a high price for this little bottle and has high expectations. Accordingly, the label should express itself and the product is worth every cent. Which it is by the way. If you would like to see the labels of the competition, just type in "CBD OIL" on "varokel.de". However, we are currently the only ones with a new filtration and the corresponding golden color. This label is going to be the base of a whole series of products. If we are happy with your label design, we will do a lot of following up designs with you. The logo design is already done and just needs to be implemented. We are looking forward to your designs. Many, many thanks in advance
Target Market(s)
Customers who want to use the absolute top CBD product on the market in order to improve their health
Colors
Requirements
Must have
- Please read the pdf-file with detailed descriptions and pictures. The costomer should always see that our product is of the highest quality. Please feel free to stick to our suggestions / ideas since I we are no designers. If you have your own cool approach, just submit it ^^
Nice to have
- We think it would be nice to have a drop out on the front of the label. We could imagine an exclusive / minimalist approach similar to Brindle

```html
<!DOCTYPE html>
<html lang="de">
<head>
<meta charset="utf-8">
<title>Aurum Select – Etiketten</title>
<link rel="stylesheet" href="https://fonts.googleapis.com/css2?family=Cinzel:wght@400&family=Montserrat:wght@400;500;700&display=swap">
<style>
  :root {
    --backdrop-top: #e2e1e2;
    --backdrop-bottom: #ffffff;
    --paper: #ffffff;
    --ink: #3a3a3a;
    --ink-soft: #555555;
    --charcoal-top: #3a3a3a;
    --charcoal-bottom: #1c1c1c;
    --rule-grey: #4d4d4d;
    --gold: #e0a025;
    --gold-deep: #d8843a;
    --gold-text: #e39a20;
    --drop-faint: #f1f1f1;
    --brown: #5a3413;
  }
  * { box-sizing: border-box; margin: 0; padding: 0; }
  html, body { width: 1200px; height: 686px; overflow: hidden; }
  body {
    background: linear-gradient(180deg, var(--backdrop-top) 0%, var(--backdrop-bottom) 40%);
    position: relative;
  }
  .label-row {
    position: absolute;
    left: 40px; top: 265px;
    width: 1120px;
    display: flex;
    justify-content: space-between;
  }
  .label { width: 340px; height: 156px; display: block; box-shadow: 0 6px 14px rgba(0,0,0,0.06); }
  .brand-name { font-family: "Cinzel", serif; fill: var(--ink); }
  .caption { font-family: "Montserrat", sans-serif; fill: var(--ink-soft); letter-spacing: 3px; }
  .strength { font-family: "Montserrat", sans-serif; font-weight: 700; }
  .side-text { font-family: "Montserrat", sans-serif; font-size: 10.5px; }
  .line-name { font-family: "Montserrat", sans-serif; font-weight: 700; letter-spacing: 3px; }
  .contents { font-family: "Montserrat", sans-serif; font-size: 6.5px; }
</style>
</head>
<body>
<main class="label-row">

  <!-- Label: charcoal variant -->
  <svg class="label label--charcoal" viewBox="0 0 653 300" xmlns="http://www.w3.org/2000/svg">
    <defs>
      <linearGradient id="charcoal" x1="0" y1="0" x2="0" y2="1">
        <stop offset="0" stop-color="var(--charcoal-top)"/>
        <stop offset="1" stop-color="var(--charcoal-bottom)"/>
      </linearGradient>
    </defs>
    <rect width="653" height="300" fill="url(#charcoal)"/>
    <path d="M0,0 H653 V10 C560,140 430,185 326,185 C222,185 93,140 0,10 Z" fill="var(--paper)"/>
    <path d="M0,17 C93,147 222,192 326,192 C430,192 560,147 653,17" fill="none" stroke="var(--rule-grey)" stroke-width="5"/>
    <path d="M0,24 C93,154 222,199 326,199 C430,199 560,154 653,24" fill="none" stroke="var(--paper)" stroke-width="2.5"/>
    <rect y="292" width="653" height="4" fill="var(--paper)"/>

    <circle cx="326" cy="50" r="14" fill="var(--gold)"/>
    <line x1="230" y1="88" x2="268" y2="88" stroke="var(--ink)" stroke-width="1"/>
    <line x1="384" y1="88" x2="422" y2="88" stroke="var(--ink)" stroke-width="1"/>
    <text class="brand-name" x="326" y="94" font-size="18" text-anchor="middle">NORDTAL</text>
    <text class="brand-name" x="326" y="114" font-size="18" text-anchor="middle">HANFWERK</text>
    <text class="caption" x="326" y="140" font-size="9" text-anchor="middle">VOLLSPEKTRUM</text>
    <text class="caption" x="326" y="155" font-size="10" text-anchor="middle">CBD-HANFÖL</text>
    <text class="strength" x="326" y="172" font-size="11" fill="var(--ink)" text-anchor="middle">10%</text>

    <path d="M326,195 C318,215 306,228 306,243 A20,20 0 0 0 346,243 C346,228 334,215 326,195 Z" fill="var(--paper)"/>
    <text class="line-name" x="326" y="276" font-size="10" fill="var(--gold-text)" text-anchor="middle">AURUM SELECT</text>
    <text class="contents" x="326" y="287" fill="var(--paper)" text-anchor="middle">10 ml · 250 Tropfen · 1000 mg CBD</text>

    <g class="side-text" fill="var(--gold-text)">
      <text transform="translate(22,288) rotate(-90)">Hergestellt in Deutschland</text>
      <text transform="translate(35,288) rotate(-90)">Produzent: Feldgrün GmbH, Aurach</text>
      <text transform="translate(48,288) rotate(-90)">Charge: 1234/2019</text>
      <text transform="translate(61,288) rotate(-90)">Mind. haltbar bis:  10/2021</text>
      <text transform="translate(597,288) rotate(-90)">Anwendung:</text>
      <text transform="translate(610,288) rotate(-90)">2 x 3 Tropfen täglich</text>
      <text transform="translate(623,288) rotate(-90)">THC-Gehalt &lt; 0,05 %</text>
      <text transform="translate(636,288) rotate(-90)">Vor Licht und Wärme schützen</text>
    </g>
  </svg>

  <!-- Label: gold variant, gold strength -->
  <svg class="label label--gold" viewBox="0 0 653 300" xmlns="http://www.w3.org/2000/svg">
    <defs>
      <linearGradient id="gold-a" x1="1" y1="0" x2="0" y2="1">
        <stop offset="0" stop-color="var(--gold)"/>
        <stop offset="1" stop-color="var(--gold-deep)"/>
      </linearGradient>
    </defs>
    <rect width="653" height="300" fill="var(--paper)"/>
    <path d="M0,254 C200,292 450,262 653,16 V300 H0 Z" fill="url(#gold-a)"/>
    <path d="M0,254 C200,292 450,262 653,16" fill="none" stroke="var(--paper)" stroke-width="4"/>
    <path d="M0,246 C200,284 450,254 653,4" fill="none" stroke="var(--gold)" stroke-width="3"/>

    <circle cx="326" cy="50" r="14" fill="var(--gold)"/>
    <line x1="240" y1="88" x2="274" y2="88" stroke="var(--ink)" stroke-width="1"/>
    <line x1="378" y1="88" x2="412" y2="88" stroke="var(--ink)" stroke-width="1"/>
    <text class="brand-name" x="326" y="94" font-size="16" text-anchor="middle">NORDTAL</text>
    <text class="brand-name" x="326" y="112" font-size="16" text-anchor="middle">HANFWERK</text>
    <text class="caption" x="326" y="137" font-size="9" text-anchor="middle">VOLLSPEKTRUM</text>
    <text class="caption" x="326" y="153" font-size="10" text-anchor="middle">CBD-HANFÖL</text>
    <path d="M288,168 C282,185 270,196 270,210 A18,18 0 0 0 306,210 C306,196 294,185 288,168 Z" fill="var(--drop-faint)"/>
    <text class="strength" x="348" y="200" font-size="14" fill="var(--gold-text)" text-anchor="middle">10%</text>

    <text class="line-name" x="326" y="276" font-size="10" fill="var(--paper)" text-anchor="middle">AURUM SELECT</text>
    <text class="contents" x="326" y="286" fill="var(--paper)" text-anchor="middle">10 ml · 250 Tropfen · 1000 mg CBD</text>

    <g class="side-text" fill="var(--gold-text)">
      <text transform="translate(22,236) rotate(-90)">Hergestellt in Deutschland</text>
      <text transform="translate(35,236) rotate(-90)">Produzent: Feldgrün GmbH, Aurach</text>
      <text transform="translate(48,236) rotate(-90)">Charge: 1234/2019</text>
      <text transform="translate(61,236) rotate(-90)">Mind. haltbar bis:  10/2021</text>
    </g>
    <g class="side-text" fill="var(--paper)">
      <text transform="translate(597,236) rotate(-90)">Anwendung:</text>
      <text transform="translate(610,236) rotate(-90)">2 x 3 Tropfen täglich</text>
      <text transform="translate(623,236) rotate(-90)">THC-Gehalt &lt; 0,05 %</text>
      <text transform="translate(636,236) rotate(-90)">Vor Licht und Wärme schützen</text>
    </g>
  </svg>

  <!-- Label: gold variant, dark strength -->
  <svg class="label label--gold-dark" viewBox="0 0 653 300" xmlns="http://www.w3.org/2000/svg">
    <defs>
      <linearGradient id="gold-b" x1="1" y1="0" x2="0" y2="1">
        <stop offset="0" stop-color="var(--gold)"/>
        <stop offset="1" stop-color="var(--gold-deep)"/>
      </linearGradient>
    </defs>
    <rect width="653" height="300" fill="var(--paper)"/>
    <path d="M0,254 C200,292 450,262 653,16 V300 H0 Z" fill="url(#gold-b)"/>
    <path d="M0,254 C200,292 450,262 653,16" fill="none" stroke="var(--paper)" stroke-width="4"/>
    <path d="M0,246 C200,284 450,254 653,4" fill="none" stroke="var(--gold)" stroke-width="3"/>

    <circle cx="326" cy="50" r="14" fill="var(--gold)"/>
    <line x1="240" y1="88" x2="274" y2="88" stroke="var(--ink)" stroke-width="1"/>
    <line x1="378" y1="88" x2="412" y2="88" stroke="var(--ink)" stroke-width="1"/>
    <text class="brand-name" x="326" y="94" font-size="16" text-anchor="middle">NORDTAL</text>
    <text class="brand-name" x="326" y="112" font-size="16" text-anchor="middle">HANFWERK</text>
    <text class="caption" x="326" y="137" font-size="9" text-anchor="middle">VOLLSPEKTRUM</text>
    <text class="caption" x="326" y="153" font-size="10" text-anchor="middle">CBD-HANFÖL</text>
    <path d="M288,168 C282,185 270,196 270,210 A18,18 0 0 0 306,210 C306,196 294,185 288,168 Z" fill="var(--drop-faint)"/>
    <text class="strength" x="348" y="200" font-size="14" fill="var(--ink)" text-anchor="middle">10%</text>

    <text class="line-name" x="326" y="276" font-size="10" fill="var(--brown)" text-anchor="middle">AURUM SELECT</text>
    <text class="contents" x="326" y="286" fill="var(--brown)" text-anchor="middle">10 ml · 250 Tropfen · 1000 mg CBD</text>

    <g class="side-text" fill="var(--gold-text)">
      <text transform="translate(22,236) rotate(-90)">Hergestellt in Deutschland</text>
      <text transform="translate(35,236) rotate(-90)">Produzent: Feldgrün GmbH, Aurach</text>
      <text transform="translate(48,236) rotate(-90)">Charge: 1234/2019</text>
      <text transform="translate(61,236) rotate(-90)">Mind. haltbar bis:  10/2021</text>
    </g>
    <g class="side-text" fill="var(--paper)">
      <text transform="translate(597,236) rotate(-90)">Anwendung:</text>
      <text transform="translate(610,236) rotate(-90)">2 x 3 Tropfen täglich</text>
      <text transform="translate(623,236) rotate(-90)">THC-Gehalt &lt; 0,05 %</text>
      <text transform="translate(636,236) rotate(-90)">Vor Licht und Wärme schützen</text>
    </g>
  </svg>

</main>
</body>
</html>
```